Vendra Corporate Letterhead

- We would like a letterhead using our logo (can be supplied as vector if needed)
- Would like to have the logo on a clear background
- Please send logo design as a separate file
- Letterhead information:
Vendra Power Inc.
482 S. Maple Ave. Suite 214
Pasadena, CA 91123

Colors
0555a3
3276b5
85abd2
000000
1b1b1b
757575
c7c7c7
e8e8e8

```html
<!DOCTYPE html>
<html lang="en">
<head>
<meta charset="utf-8">
<title>Vendra Corporate Letterhead</title>
<link href="https://fonts.googleapis.com/css2?family=Open+Sans:wght@400;600&display=swap" rel="stylesheet">
<style>
  :root {
    --blue-deep: #0555a3;
    --blue-mid: #3276b5;
    --blue-light: #85abd2;
    --ink: #1b1b1b;
    --grey-dark: #757575;
    --grey-mid: #c7c7c7;
    --grey-light: #e8e8e8;
    --backdrop: #eeeeee;
    --paper: #ffffff;
  }
  * { margin: 0; padding: 0; box-sizing: border-box; }
  html, body { width: 1200px; height: 795px; overflow: hidden; }
  body {
    background: var(--backdrop);
    font-family: "Open Sans", Arial, sans-serif;
    color: var(--ink);
    display: flex;
    align-items: center;
    justify-content: center;
  }
  .letterhead {
    position: relative;
    width: 540px;
    height: 764px;
    background: var(--paper);
    box-shadow: 0 2px 10px rgba(0,0,0,0.12);
    overflow: hidden;
  }
  .corner-band {
    position: absolute;
    left: 0;
    top: 0;
    width: 540px;
    height: 764px;
  }
  .brand {
    position: absolute;
    top: 62px;
    left: 56px;
    display: flex;
    align-items: center;
    gap: 7px;
  }
  .brand-dot {
    width: 12px; height: 12px;
    border-radius: 50%;
    background: var(--blue-deep);
  }
  .brand-name {
    font-size: 26px;
    font-weight: 600;
    color: var(--blue-deep);
    letter-spacing: 0.5px;
  }
  .letter-body {
    position: absolute;
    top: 150px;
    left: 70px;
    width: 350px;
  }
  .salutation {
    font-size: 14px;
    margin-bottom: 16px;
  }
  .letter-body p {
    font-size: 8.5px;
    line-height: 13px;
    color: var(--ink);
    margin-bottom: 13px;
  }
  .closing {
    position: absolute;
    top: 470px;
    left: 70px;
    font-size: 9px;
    color: var(--ink);
  }
  .signature {
    display: block;
    width: 70px;
    height: 26px;
    margin: 8px 0 6px 46px;
    background: var(--grey-light);
  }
  .signer { margin-left: 46px; line-height: 13px; }
  .company-block {
    position: absolute;
    right: 22px;
    bottom: 60px;
    text-align: right;
    color: var(--paper);
    font-size: 10px;
    line-height: 14px;
    font-style: normal;
  }
  .company-name { font-weight: 600; font-size: 11px; }
</style>
</head>
<body>
  <main class="letterhead">
    <svg class="corner-band" viewBox="0 0 540 764" aria-hidden="true">
      <defs>
        <linearGradient id="bandShade" x1="0" y1="0" x2="1" y2="1">
          <stop offset="0" stop-color="#c7c7c7"/>
          <stop offset="1" stop-color="#757575"/>
        </linearGradient>
      </defs>
      <path d="M540 400 L540 764 L290 764 C 320 690, 335 560, 375 470 C 395 425, 465 400, 540 400 Z" fill="url(#bandShade)"/>
    </svg>

    <header class="brand">
      <span class="brand-dot"></span>
      <span class="brand-name">Vendra</span>
    </header>

    <section class="letter-body">
      <div class="salutation">Dear Mr. Reyes,</div>
      <p>We are pleased to confirm our partnership for the coming season and look forward to working closely with your team. Our engineers will review the site plans this month and share a complete schedule, budget notes and supply details before the next meeting.</p>
      <p>Please find the signed agreement enclosed with this letter. Our finance office will issue the first invoice once the installation dates are set, and a project lead will contact you to arrange a short call.</p>
      <p>During the first phase we will test every unit on site and record the results in a shared report. Any changes to the scope can be raised with our office at any time, and we will respond within two working days.</p>
      <p>It is a long established fact that a reader will be distracted by the readable content of a page when looking at its layout. The point of using Lorem Ipsum is that it has a more-or-less normal distribution of letters, as opposed to using 'Content here, content here', making it look like readable English. Many desktop publishing packages.</p>
    </section>

    <footer class="closing">
      <div>Sincerely,</div>
      <span class="signature" role="img" aria-label="Handwritten signature"></span>
      <div class="signer">Daniel Reyes<br>CEO/ Founder</div>
    </footer>

    <address class="company-block">
      <div class="company-name">Vendra Power Inc.</div>
      <div>482 S. Maple Ave.</div>
      <div>Suite 214, Pasadena, CA 91123</div>
    </address>
  </main>
</body>
</html>
```